Life Coach for Lawyers Business Card Design

Elegant, original, business card design for life coaching service for associate attorneys who work in big law and struggle with stress, overwhelm, and time management. Double sided design.

Target Market(s)

Women associate attorneys who work in big law and struggle with stress, overwhelm, and time management.

Industry/Entity Type

Life Coaching

Contact Information for Business Card

Marissa Pendrell
Life Coach
518.677.3941
calmbriefcounsel.net
marissa@calmbriefcounsel.net
@calmbriefcounsel (Instagram)

Font styles to use
Other font styles liked:
• Silver South font duo. See uploaded files.

Requirements
Must have
• Icons for phone, website, email, and Instagram instead of words. Specific colors used in my logo (171B2B, 421121, FFFFFF)
Nice to have
• Foil. Embossed. Feminine design.
Should not have
• Any colors other than those used in logo. See uploaded files.

```html
<!DOCTYPE html>
<html lang="en">
<head>
<meta charset="utf-8">
<title>Calm Brief Counsel – Business Card</title>
<link href="https://fonts.googleapis.com/css2?family=Roboto:wght@300;400;700&display=swap" rel="stylesheet">
<style>
  :root {
    --navy: #171B2B;
    --wine: #421121;
    --wine-deep: #350d1a;
    --white: #FFFFFF;
  }
  * { box-sizing: border-box; margin: 0; padding: 0; }
  html, body { width: 1200px; height: 900px; overflow: hidden; }
  body {
    background: var(--navy);
    font-family: "Roboto", Arial, sans-serif;
    color: var(--white);
    position: relative;
  }
  .card {
    position: absolute;
    top: 295px;
    width: 540px;
    height: 310px;
    border-radius: 18px;
    background: linear-gradient(160deg, var(--wine) 0%, var(--wine-deep) 100%);
    overflow: hidden;
  }
  .card-front { left: 40px; }
  .card-back { left: 620px; }

  .brand-name {
    font-family: "Roboto", Arial, sans-serif;
    font-weight: 300;
    color: var(--white);
    text-transform: uppercase;
    letter-spacing: 0.12em;
    line-height: 1.1;
  }
  .front-brand {
    position: absolute;
    left: 34px;
    top: 30px;
    font-size: 22px;
  }

  .contact-list {
    position: absolute;
    left: 34px;
    top: 150px;
    list-style: none;
    font-weight: 300;
    font-size: 13px;
  }
  .contact-list li {
    display: flex;
    align-items: center;
    gap: 10px;
    height: 24px;
    white-space: nowrap;
  }
  .contact-list svg { width: 13px; height: 13px; flex: none; }

  .person {
    position: absolute;
    right: 34px;
    top: 130px;
    text-align: right;
  }
  .person-name {
    font-weight: 700;
    font-size: 25px;
    letter-spacing: 0.01em;
    white-space: nowrap;
  }
  .person-role {
    font-weight: 700;
    font-size: 19px;
    margin-top: 4px;
  }
  .person-rule {
    height: 2px;
    width: 250px;
    background: var(--white);
    margin: 8px 0 0 auto;
  }

  .seal {
    position: absolute;
    right: 34px;
    bottom: 26px;
    display: flex;
    align-items: center;
    gap: 8px;
  }
  .seal-dot {
    width: 12px; height: 12px;
    border: 1px solid var(--white);
    border-radius: 50%;
    flex: none;
  }
  .seal-name {
    font-size: 10px;
    white-space: nowrap;
  }

  .back-band {
    position: absolute;
    left: 36px;
    top: 0;
    width: 26px;
    height: 100%;
    background: var(--white);
    display: flex;
    align-items: center;
    justify-content: center;
  }
  .back-band-text {
    transform: rotate(90deg);
    white-space: nowrap;
    color: var(--wine);
    font-size: 11px;
    font-weight: 400;
    display: flex;
    align-items: center;
    gap: 6px;
  }
  .back-band-text svg { width: 11px; height: 11px; }
  .back-brand {
    position: absolute;
    left: 62px;
    right: 0;
    top: 50%;
    transform: translateY(-50%);
    text-align: center;
    font-size: 34px;
  }
</style>
</head>
<body>
  <section class="card card-front">
    <div class="brand-name front-brand">Calm Brief<br>Counsel</div>

    <ul class="contact-list">
      <li>
        <svg viewBox="0 0 24 24" fill="#FFFFFF"><path d="M6.6 10.8a15.1 15.1 0 0 0 6.6 6.6l2.2-2.2c.3-.3.7-.4 1-.2 1.1.4 2.3.6 3.6.6.6 0 1 .4 1 1V20c0 .6-.4 1-1 1A17 17 0 0 1 3 4c0-.6.4-1 1-1h3.5c.6 0 1 .4 1 1 0 1.3.2 2.5.6 3.6.1.3 0 .7-.2 1z"/></svg>
        518.677.3941
      </li>
      <li>
        <svg viewBox="0 0 24 24" fill="none" stroke="#FFFFFF" stroke-width="2"><circle cx="12" cy="12" r="10"/><path d="M2 12h20M12 2c3 3 3 17 0 20M12 2c-3 3-3 17 0 20"/></svg>
        calmbriefcounsel.net
      </li>
      <li>
        <svg viewBox="0 0 24 24" fill="none" stroke="#FFFFFF" stroke-width="2"><path d="M2 5h20v14H2z"/><path d="M2 5l10 8 10-8"/></svg>
        marissa@calmbriefcounsel.net
      </li>
      <li>
        <svg viewBox="0 0 24 24" fill="none" stroke="#FFFFFF" stroke-width="2"><circle cx="12" cy="12" r="9"/></svg>
        @calmbriefcounsel
      </li>
    </ul>

    <div class="person">
      <div class="person-name">Marissa Pendrell</div>
      <div class="person-role">Life Coach</div>
      <div class="person-rule"></div>
    </div>

    <div class="seal">
      <span class="seal-dot"></span>
      <span class="brand-name seal-name">Calm Brief Counsel</span>
    </div>
  </section>

  <section class="card card-back">
    <div class="back-band">
      <div class="back-band-text">
        <svg viewBox="0 0 24 24" fill="none" stroke="#421121" stroke-width="2"><circle cx="12" cy="12" r="10"/><path d="M2 12h20M12 2c3 3 3 17 0 20M12 2c-3 3-3 17 0 20"/></svg>
        calmbriefcounsel.net
      </div>
    </div>
    <div class="brand-name back-brand">Calm Brief<br>Counsel</div>
  </section>
</body>
</html>
```